Varnath Consulting Business card design.

See our website www.varnathconsulting-example.com which will give you a good idea of what we are about. The font is called 'Play'.

I'd like a standout business card in keeping with the themes and branding on the website

Target Market(s)

professionals. HR directors

Industry/Entity Type

Business

Contact Information for Business Card

Varnath Consulting PO Box 3917 Tindale Creek NSW 2840 1300 457 318 Gerald Ashbury Principal email: jobs@varnathconsulting-example.com ABN: 31792048663

Font styles to use
Other font styles liked:
• Play

Requirements
Must have
• Must have same design colours and branding as website.
• On back I'd prefer a list of the things we do which appears below the name at the header on the website

```html
<!DOCTYPE html>
<html lang="en">
<head>
<meta charset="utf-8">
<title>Varnath Consulting – Business Card</title>
<link href="https://fonts.googleapis.com/css2?family=Play:wght@400;700&display=swap" rel="stylesheet">
<style>
  :root {
    --page: #d9dbde;
    --navy: #0a1f33;
    --blue: #1e8fe0;
    --white: #ffffff;
    --photo-dark: #0d1a26;
    --photo-skin: #a87a6e;
    --photo-track: #7a3a30;
  }
  * { margin: 0; padding: 0; box-sizing: border-box; }
  html, body { width: 1189px; height: 1200px; overflow: hidden; }
  body {
    background: var(--page);
    font-family: 'Play', sans-serif;
    position: relative;
  }
  .card {
    position: absolute;
    left: 136px;
    width: 918px;
    height: 524px;
    background: var(--navy);
    overflow: hidden;
  }
  .card--front { top: 45px; }
  .card--back { top: 600px; }

  .brand {
    position: absolute;
    color: var(--white);
    font-size: 67px;
    font-weight: 400;
    letter-spacing: 1px;
    line-height: 1;
    white-space: nowrap;
  }
  .tagline {
    position: absolute;
    color: var(--blue);
    font-size: 19px;
    letter-spacing: 2.6px;
    line-height: 1;
    white-space: nowrap;
  }
  .tagline .sep { color: var(--white); opacity: .8; margin: 0 6px; }

  .card--front .brand { left: 78px; top: 60px; }
  .card--front .tagline { left: 76px; top: 150px; }

  .person-name {
    position: absolute; left: 74px; top: 218px;
    color: var(--blue); font-size: 33px; line-height: 1;
  }
  .person-role {
    position: absolute; left: 74px; top: 259px;
    color: var(--white); font-size: 26px; line-height: 1;
  }
  .abn {
    position: absolute; left: 76px; top: 326px;
    color: var(--white); font-size: 23px; line-height: 1;
  }
  .contact-list { position: absolute; left: 75px; top: 362px; list-style: none; }
  .contact-list li {
    display: flex; align-items: center;
    height: 40px;
    color: var(--white); font-size: 23px;
  }
  .contact-list svg { width: 18px; height: 18px; margin-right: 22px; flex: none; }

  .card--back .header { position: absolute; left: 0; top: 0; width: 100%; height: 159px; }
  .card--back .brand { left: 0; width: 100%; text-align: center; top: 30px; }
  .card--back .tagline { left: 0; width: 100%; text-align: center; top: 116px; }
  .photo {
    position: absolute; left: 0; top: 159px; width: 100%; height: 365px;
    background:
      linear-gradient(180deg, rgba(13,26,38,0) 55%, var(--photo-track) 80%, #5e2c26 100%),
      linear-gradient(90deg, var(--photo-dark) 0%, var(--photo-dark) 18%, var(--photo-skin) 40%, #c49486 60%, #8d5f55 85%, #b98a7e 100%);
  }
</style>
</head>
<body>
  <section class="card card--front">
    <div class="brand">VARNATH CONSULTING</div>
    <div class="tagline">Search &amp; Select<span class="sep">|</span>Career<span class="sep">|</span>Coaching<span class="sep">|</span>Leadership<span class="sep">|</span>Outplacement</div>
    <div class="person-name">Gerald Ashbury</div>
    <div class="person-role">Principal</div>
    <div class="abn">ABN: 31792048663</div>
    <ul class="contact-list">
      <li>
        <svg viewBox="0 0 18 18" aria-hidden="true"><rect width="18" height="18" fill="#1e8fe0"/><path d="M5 3.5l2.5 0 1 3-1.5 1.2c.8 1.6 1.7 2.5 3.3 3.3L11.5 9.5l3 1v2.5c-5.5.5-10-4-9.5-9.5z" fill="#0a1f33"/></svg>
        1300 457 318
      </li>
      <li>
        <svg viewBox="0 0 18 18" aria-hidden="true"><rect width="18" height="18" fill="#1e8fe0"/><rect x="3.5" y="5" width="11" height="8" fill="none" stroke="#0a1f33" stroke-width="1.4"/><path d="M3.5 5l5.5 4.5 5.5-4.5" fill="none" stroke="#0a1f33" stroke-width="1.4"/></svg>
        jobs@varnathconsulting-example.com
      </li>
      <li>
        <svg viewBox="0 0 18 18" aria-hidden="true"><rect width="18" height="18" fill="#1e8fe0"/><path d="M9 3.5a3.6 3.6 0 0 1 3.6 3.6c0 2.6-3.6 7-3.6 7s-3.6-4.4-3.6-7A3.6 3.6 0 0 1 9 3.5z" fill="#0a1f33"/><circle cx="9" cy="7.1" r="1.3" fill="#1e8fe0"/></svg>
        PO Box 3917&nbsp; Tindale Creek NSW 2840
      </li>
    </ul>
  </section>

  <section class="card card--back">
    <div class="header">
      <div class="brand">VARNATH CONSULTING</div>
      <div class="tagline">Search &amp; Select<span class="sep">|</span>Career<span class="sep">|</span>Coaching<span class="sep">|</span>Leadership<span class="sep">|</span>Outplacement</div>
    </div>
    <div class="photo" role="img" aria-label="Photograph of sprinters' hands set on the start line of a running track"></div>
  </section>
</body>
</html>
```